Vireo Halden Business Cards

Vireo Halden Luxury Brand Collection is a global representation business focusing on high end luxury. We need business cards to epitomize our global, luxury delivery model.

Target Market(s)

Global Representation in the hospitality industry

Industry/Entity Type

Hospitality

Contact Information for Business Card

name
title
email: first.last@vh-kmt.com
web: www.vh-kmt.com
mobile:

Requirements
Must have
• double sided design
• incorporate logo colours
• have logo prominent
Should not have
• no designs not incorporating logo colours.

```html
<!DOCTYPE html>
<html lang="en">
<head>
<meta charset="utf-8">
<title>Vireo Halden Business Cards</title>
<link rel="stylesheet" href="https://fonts.googleapis.com/css2?family=Lato:wght@300;400;700&display=swap">
<style>
  :root {
    --gold: #7d6a3e;
    --espresso: #352c2c;
    --card: #bfb4a1;
    --white: #ffffff;
  }
  * { box-sizing: border-box; margin: 0; padding: 0; }
  html, body { width: 1200px; height: 1200px; overflow: hidden; }
  body {
    position: relative;
    font-family: "Lato", sans-serif;
    background: linear-gradient(to bottom left, var(--espresso) 50%, var(--gold) 50%);
  }
  .card {
    position: absolute;
    left: 179px;
    width: 841px;
    height: 481px;
    background: var(--card);
    color: var(--gold);
  }
  .card--front { top: 98px; }
  .card--back { top: 622px; }

  .brand-name {
    position: absolute;
    font-weight: 700;
    color: var(--gold);
    white-space: nowrap;
    line-height: 1;
  }
  .card--front .brand-name {
    right: 40px;
    top: 160px;
    font-size: 48px;
  }
  .card--back .brand-name {
    left: 0; right: 0;
    top: 205px;
    text-align: center;
    font-size: 72px;
  }

  .person-name {
    position: absolute;
    left: 30px;
    top: 278px;
    font-size: 35px;
    font-weight: 700;
    letter-spacing: -0.5px;
    text-transform: uppercase;
  }
  .person-title {
    position: absolute;
    left: 30px;
    top: 324px;
    font-size: 25px;
    font-weight: 700;
  }
  .divider {
    position: absolute;
    left: 30px;
    top: 351px;
    width: 765px;
    height: 2px;
    background: var(--gold);
  }
  .contact-list {
    position: absolute;
    right: 84px;
    top: 362px;
    list-style: none;
    text-align: right;
    font-size: 23px;
    font-weight: 400;
    line-height: 29px;
  }
  .contact-icons {
    position: absolute;
    left: 767px;
    top: 358px;
    width: 33px;
    height: 93px;
    background: var(--gold);
    display: flex;
    flex-direction: column;
    align-items: center;
    justify-content: space-around;
    padding: 3px 0;
  }
  .contact-icons svg { display: block; }
</style>
</head>
<body>
  <section class="card card--front" aria-label="Business card front">
    <div class="brand-name">Vireo Halden</div>
    <h1 class="person-name">Maren Solvik</h1>
    <p class="person-title">Director</p>
    <div class="divider"></div>
    <ul class="contact-list">
      <li>+123-555-0147</li>
      <li>first.last@vh-kmt.com</li>
      <li>www.vh-kmt.com</li>
    </ul>
    <div class="contact-icons">
      <svg width="14" height="24" viewBox="0 0 14 24" aria-label="Mobile">
        <rect x="1" y="1" width="12" height="22" rx="2" fill="none" stroke="#fff" stroke-width="2"/>
        <circle cx="7" cy="19.5" r="1.3" fill="#fff"/>
      </svg>
      <svg width="20" height="14" viewBox="0 0 20 14" aria-label="Email">
        <rect x="0" y="0" width="20" height="14" rx="2" fill="#fff"/>
        <path d="M1 1 L10 8 L19 1" fill="none" stroke="#7d6a3e" stroke-width="1.6"/>
      </svg>
      <svg width="20" height="20" viewBox="0 0 20 20" aria-label="Website">
        <circle cx="10" cy="10" r="9" fill="#fff"/>
        <path d="M5 6 Q8 4 10 7 Q8 10 6 9 Z M11 11 Q14 10 15 13 Q13 16 11 15 Z" fill="#7d6a3e"/>
      </svg>
    </div>
  </section>

  <section class="card card--back" aria-label="Business card back">
    <div class="brand-name">Vireo Halden</div>
  </section>
</body>
</html>
```